Bref créative
Law firm stationary package
Letterhead, business card, envelope
Professional
Theodore R. Wexley
Attorney at Law
5183 Poldin Lane, Suite A
P.O. Box 81947
Cincinnati, OH 45867
Ted@WexleyCounsel.example
www.WexleyCounsel.example
Please create business card, letterhead, and envelope designs.
Focus on clean, professional design for this corporate law firm. Stay away from watermarks, waves, or anything that is too ink-intensive. You may use either or both of the attached logos.
Main logo
Inverse of logo, use is optional

```html
<!DOCTYPE html>
<html lang="en">
<head>
<meta charset="utf-8">
<title>Wexley Counsel — Stationery Concepts</title>
<link rel="stylesheet" href="https://fonts.googleapis.com/css2?family=Cinzel:wght@400;600&family=Cormorant+SC:wght@500&family=Lato:wght@400;700&display=swap">
<style>
  :root {
    --backdrop: #dccbae;
    --paper: #fbfbfa;
    --paper-edge: #e3e1dc;
    --navy: #26226f;
    --navy-deep: #1d1a5c;
    --ink: #4a4a55;
    --muted: #8a8a94;
    --label: #3e3a33;
  }
  * { box-sizing: border-box; margin: 0; padding: 0; }
  html, body { width: 1200px; height: 624px; overflow: hidden; }
  body {
    position: relative;
    background: var(--backdrop);
    font-family: "Lato", sans-serif;
    color: var(--ink);
  }
  .caption {
    position: absolute;
    font-family: "Cormorant SC", serif;
    font-weight: 500;
    font-size: 12px;
    letter-spacing: 0.6px;
    color: var(--label);
    text-align: center;
    white-space: nowrap;
  }
  .sheet {
    position: absolute;
    background: var(--paper);
    box-shadow: 0 2px 6px rgba(60, 45, 25, 0.28);
  }

  /* Brand lockup */
  .brand { display: flex; align-items: center; gap: 8px; color: var(--navy); }
  .brand__mark { background: var(--navy); flex: none; }
  .brand__text { font-family: "Cinzel", serif; font-weight: 400; line-height: 1; }
  .brand__name { display: block; letter-spacing: 0.5px; }
  .brand__sub { display: block; letter-spacing: 1.5px; margin-top: 3px; }
  .brand--inverse { color: #ffffff; }
  .brand--inverse .brand__mark { background: #ffffff; }

  /* Business card front */
  .card-front { left: 24px; top: 221px; width: 175px; height: 101px; padding: 12px 12px; }
  .card-front .brand__mark { width: 14px; height: 14px; }
  .card-front .brand__name { font-size: 12px; }
  .card-front .brand__sub { font-size: 4px; }
  .card-front__person { position: absolute; left: 12px; top: 50px; }
  .card-front__name { font-size: 6px; font-weight: 700; color: var(--navy); }
  .card-front__role { font-size: 4.5px; color: var(--muted); margin-top: 1px; }
  .card-front__contact { position: absolute; left: 92px; top: 46px; list-style: none; }
  .card-front__contact li { font-size: 4px; line-height: 6.4px; color: var(--ink); display: flex; align-items: center; gap: 3px; }
  .card-front__contact li::before { content: ""; width: 3px; height: 3px; background: var(--navy); }
  .card-front__rule { position: absolute; left: 0; right: 0; bottom: 0; height: 4px; background: var(--navy); }

  /* Business card back */
  .card-back { left: 24px; top: 348px; width: 175px; height: 101px; background: var(--navy); display: flex; align-items: center; justify-content: center; }
  .card-back .brand__mark { width: 20px; height: 20px; }
  .card-back .brand__name { font-size: 17px; }
  .card-back .brand__sub { font-size: 5px; }

  /* Letterhead */
  .letterhead { left: 230px; top: 24px; width: 423px; height: 545px; }
  .letterhead .brand { position: absolute; left: 24px; top: 19px; gap: 10px; }
  .letterhead .brand__mark { width: 18px; height: 18px; }
  .letterhead .brand__name { font-size: 19px; }
  .letterhead .brand__sub { font-size: 5px; }
  .letterhead__footer { position: absolute; left: 0; right: 0; bottom: 17px; height: 14px; background: var(--navy); border-top: 2px solid #5d5aa6; display: flex; align-items: center; justify-content: space-between; padding: 0 14px; }
  .letterhead__footer span { font-size: 4.6px; color: #ffffff; letter-spacing: 0.2px; display: flex; align-items: center; gap: 3px; }
  .letterhead__footer span::before { content: ""; width: 3px; height: 3px; background: #ffffff; }
  .letterhead__foot-rule { position: absolute; left: 0; right: 0; bottom: 12px; height: 2px; background: var(--navy-deep); }

  /* Envelopes */
  .envelope { left: 679px; width: 473px; height: 204px; }
  .envelope--back { top: 132px; }
  .envelope__flap { position: absolute; inset: 0; }
  .envelope--back .brand { position: absolute; left: 224px; top: 34px; }
  .envelope--back .brand__mark { width: 22px; height: 22px; }
  .envelope--front { top: 367px; }
  .envelope--front .brand { position: absolute; left: 22px; top: 36px; gap: 7px; }
  .envelope--front .brand__mark { width: 12px; height: 12px; }
  .envelope--front .brand__name { font-size: 11px; }
  .envelope--front .brand__sub { font-size: 3.5px; }
  .envelope__return { position: absolute; left: 41px; top: 58px; font-size: 4px; color: var(--muted); }
</style>
</head>
<body>

  <p class="caption" style="left:22px; top:158px; width:180px;">Stationery Concepts</p>

  <section class="sheet card-front" aria-label="Business card front">
    <div class="brand">
      <span class="brand__mark"></span>
      <span class="brand__text"><span class="brand__name">WEXLEY</span><span class="brand__sub">COUNSEL, LLC</span></span>
    </div>
    <div class="card-front__person">
      <p class="card-front__name">Theodore R. Wexley</p>
      <p class="card-front__role">Attorney at Law</p>
    </div>
    <ul class="card-front__contact">
      <li>5183 Poldin Lane, Suite A</li>
      <li>P.O. Box 81947</li>
      <li>Cincinnati, OH 45867</li>
      <li>P 513.555.0142</li>
      <li>F 513.555.0143</li>
      <li>Ted@WexleyCounsel.example</li>
    </ul>
    <div class="card-front__rule"></div>
  </section>
  <p class="caption" style="left:22px; top:330px; width:180px;">Business Card Front</p>

  <section class="sheet card-back" aria-label="Business card back">
    <div class="brand brand--inverse">
      <span class="brand__mark"></span>
      <span class="brand__text"><span class="brand__name">WEXLEY</span><span class="brand__sub">COUNSEL, LLC</span></span>
    </div>
  </section>
  <p class="caption" style="left:22px; top:457px; width:180px;">Business Card Back</p>

  <section class="sheet letterhead" aria-label="Letterhead">
    <div class="brand">
      <span class="brand__mark"></span>
      <span class="brand__text"><span class="brand__name">WEXLEY</span><span class="brand__sub">COUNSEL, LLC</span></span>
    </div>
    <div class="letterhead__footer">
      <span>5183 Poldin Lane, Suite A · P.O. Box 81947 · Cincinnati, OH 45867</span>
      <span>P 513.555.0142</span>
      <span>F 513.555.0143</span>
      <span>Ted@WexleyCounsel.example</span>
      <span>www.WexleyCounsel.example</span>
    </div>
    <div class="letterhead__foot-rule"></div>
  </section>
  <p class="caption" style="left:341px; top:582px; width:200px;">Letter Head Option 1</p>

  <section class="sheet envelope envelope--back" aria-label="Envelope back">
    <svg class="envelope__flap" width="473" height="204" viewBox="0 0 473 204" aria-hidden="true">
      <polyline points="2,2 236,86 471,2" fill="none" stroke="#d8d6d1" stroke-width="1.2"/>
      <line x1="2" y1="202" x2="190" y2="120" stroke="#ecebe7" stroke-width="1"/>
      <line x1="471" y1="202" x2="283" y2="120" stroke="#ecebe7" stroke-width="1"/>
    </svg>
    <div class="brand"><span class="brand__mark"></span></div>
  </section>

  <section class="sheet envelope envelope--front" aria-label="Envelope front">
    <div class="brand">
      <span class="brand__mark"></span>
      <span class="brand__text"><span class="brand__name">WEXLEY</span><span class="brand__sub">COUNSEL, LLC</span></span>
    </div>
    <p class="envelope__return">5183 Poldin Lane, Suite A · Cincinnati, OH 45867</p>
  </section>
  <p class="caption" style="left:815px; top:582px; width:200px;">Envelope Option 2</p>

</body>
</html>
```